Lively Civic Layout Workshop needs a Flyer design

I created Plazamesh Kit, a tool that enables public participation for urban planning project. We enable people to get together to do collaborative urban design. We use the tool by organizing a workshop at a local community centre or a office. The workshop is a fun interactive way to engage with citizens on urban planning projects. Think of Doodle Among Pals except more like Urban Design with Friends.

This workshop is what I am trying to pitch for companies, architects and planning agencies in cities. I am looking to make a flyer that I can hand to professionals at conferences or send them via email. It should inform them about workshop and get them interested in reaching out or show it to their boss.

I have a sample of a flyer design attached. Don't worry about the text, It shows the look and feel that I am aiming for: sleek, minimal colors, to the point and modern. This flyer is going to be distributed to professionals in companies (architects, urban planners and landscape planners). It should communicate the workshop and the value proposition with text and imagery / icons.

There has to be a balance of text and visuals. I am happy if we use icons, since the workshop is interactive and people coming together to sketch urban designs on map and the flyer should communicate that.

Here are some photos I got off the internet to communicate what happens in the workshop:

Image 1 : http://www.kestrelvale.edu/architecture/rkpm/senvora/images/engagement_02.jpg
Image 2: http://www.brindlequay.com/files/tolvo-3_0.png
Image 3: http://www.marlowgate.com/assets/img/pages/processes/public-realm-movement-strategy-open-studio-development-workshop-marlowgate-engagement-involvement-urban-design-analysis.jpg

The final flyer should be two pages long all the text for the flyer is in pmk-1-page-text.pdf attached. It needs to be formatted and fit in well.
Updates

Guys, after reviewing the brief, just a quick update, you dont have to use all the text provided, you can remove some text if you prefer. 

Target Market(s)

The target audience of this flyer is architects, urban planners, landscape planners, planning officers in cities. Usually they would be college educated having degrees in Urban planning, landscape planning or architecture. They would be interested in Urban design. The age group is diverse anywhere from 21-71.

They may have to show this flyer to their boss either in person or over email. After sending this flyer around, they are expected to email us or reach out to us saying they are interested to know more or have a conversation about organising the workshop.

Industry/Entity Type

Landscape

Font styles to use
Sans Serif

Colors
33a6d7
3176b5
fece3e
919191
efefef
86cae6
fde08a
faa54b

Requirements
Must have
• - It should communicate, modernism, minimalism and futuristic design
- It should be two pages
Should not have
• - Too many pictures of faces / people
- Heavy and old fashoined fonts.

```html
<!DOCTYPE html>
<html lang="en">
<head>
<meta charset="utf-8">
<title>Plazamesh Kit – Workshop Flyer</title>
<link rel="stylesheet" href="https://fonts.googleapis.com/css2?family=Jost:wght@300;400&display=swap">
<style>
  :root {
    --backdrop: #d8d6d3;
    --paper: #ffffff;
    --band: #bdbcbb;
    --sky: #8cc6e6;
    --accent: #55ade0;
    --ink: #2c2c2c;
    --ink-soft: #3a3a3a;
    --icon-dark: #444444;
    --photo: #8a7a6e;
  }
  * { box-sizing: border-box; margin: 0; padding: 0; }
  html, body {
    width: 1200px; height: 838px; overflow: hidden;
    background: var(--backdrop);
    font-family: "Jost", "Futura", sans-serif;
    font-weight: 300;
    color: var(--ink);
  }
  h1, h2, h3 { font-weight: 300; }
  .page {
    position: absolute; top: 23px;
    width: 556px; height: 785px;
    background: var(--paper);
    box-shadow: 0 3px 10px rgba(0,0,0,.25);
  }
  .page--front { left: 28px; }
  .page--back  { left: 617px; }
  .abs { position: absolute; }

  /* Brand */
  .brand { left: 40px; top: 45px; display: flex; align-items: center; gap: 8px; }
  .brand__dot { width: 13px; height: 13px; border-radius: 50%; background: var(--sky); }
  .brand__name { font-size: 19px; font-weight: 400; color: var(--accent); letter-spacing: .4px; }
  .tagline { left: 234px; top: 36px; font-size: 16.5px; line-height: 19.5px; color: var(--ink-soft); }

  /* Band */
  .band { left: 0; width: 100%; background: var(--band); color: #fff; padding: 10px 34px 0; }
  .band__title { font-size: 17px; margin-bottom: 3px; }
  .band__text { font-size: 10.5px; line-height: 13px; }
  .page--front .band { top: 93px; height: 81px; }
  .page--back .band { top: 33px; height: 82px; padding-top: 13px; }

  .belief { left: 0; width: 100%; top: 189px; text-align: center; font-size: 11px; }
  .icon { position: absolute; }

  .audience {
    position: absolute; top: 255px; height: 107px; width: 238px;
    background: var(--sky); border-radius: 12px; color: #fff;
    font-size: 10.5px; line-height: 14px; padding: 13px 18px 0 18px;
  }
  .audience--citizens { left: 34px; }
  .audience--pros { left: 285px; }

  .label { color: var(--accent); font-size: 11px; font-weight: 300; }
  .body { font-size: 10.5px; line-height: 14px; }

  .how-title { left: 34px; top: 382px; }
  .how-intro { left: 34px; top: 397px; width: 500px; }

  .step-icon { position: absolute; top: 440px; width: 65px; height: 65px; border-radius: 50%; background: var(--sky); }
  .step-caption { position: absolute; top: 516px; width: 128px; }

  .lead { left: 34px; top: 597px; }
  .feature { position: absolute; width: 232px; }
  .feature .label { display: block; }

  /* Back page */
  .section { position: absolute; width: 228px; }
  .section__head { display: flex; align-items: center; gap: 6px; font-size: 12.5px; font-weight: 300; margin-bottom: 2px; letter-spacing: .2px; }
  .num { width: 15px; height: 15px; border-radius: 50%; background: var(--sky); color: #fff; font-size: 10px; display: flex; align-items: center; justify-content: center; }
  .item { padding-left: 21px; margin-bottom: 6px; }
  .item .label { display: block; line-height: 14px; }

  .when-title { left: 34px; top: 511px; font-size: 11.5px; }
  .when-text { left: 34px; top: 532px; width: 500px; }
  .accel-title { left: 34px; top: 569px; }
  .accel-text { left: 34px; top: 583px; width: 500px; }

  .callout { left: 229px; top: 620px; width: 264px; height: 107px; background: var(--sky); border-radius: 10px; color: #fff; padding: 11px 22px 0 26px; }
  .callout__title { font-size: 16px; margin-bottom: 3px; }
  .callout__text { font-size: 10px; line-height: 13px; }
  .callout__email { font-size: 11px; margin-top: 5px; }
  .contact-ring { left: 75px; top: 610px; width: 140px; height: 140px; border-radius: 50%; background: var(--sky); }
  .contact-photo { left: 91px; top: 626px; width: 108px; height: 108px; border-radius: 50%; background: radial-gradient(circle at 50% 40%, #a39283, var(--photo)); border: 3px solid #fff; }
</style>
</head>
<body>

<section class="page page--front">
  <div class="abs brand"><span class="brand__dot"></span><span class="brand__name">Plazamesh Kit</span></div>
  <p class="abs tagline">Feel the pulse of those directly affected<br>by your next urban design project</p>

  <header class="abs band">
    <h1 class="band__title">Crowdsourced Urban Planning</h1>
    <p class="band__text">Plazamesh Kit is a technology-powered platform for urban planning professionals to easily collaborate with non-experts and ordinary citizens on urban planning projects.</p>
  </header>

  <p class="abs belief">At Plazamesh Kit, we believe that everyone can be an urban designer.</p>

  <div class="icon" role="img" aria-label="Pictogram of a group of citizens" style="left:122px;top:214px;width:60px;height:31px;background:var(--icon-dark);border-radius:8px 8px 2px 2px;"></div>
  <svg class="icon" style="left:379px;top:211px" width="50" height="34" viewBox="0 0 50 40" preserveAspectRatio="none" aria-label="City buildings icon" role="img">
    <rect x="2" y="16" width="9" height="24" fill="var(--icon-dark)"/>
    <path d="M14 8 L28 0 V40 H14 Z" fill="var(--icon-dark)"/>
    <rect x="31" y="6" width="8" height="34" fill="var(--icon-dark)"/>
    <rect x="41" y="12" width="8" height="28" fill="var(--icon-dark)"/>
  </svg>

  <p class="audience audience--citizens">For citizens, it is a community-driven exercise to showcase and share creative ideas for their neighborhood and have a forum for engaged, data driven discussions that go beyond the rhetoric</p>
  <p class="audience audience--pros">For companies, architects, planners and city agencies, we provide an easy way to show their commitment to all stakeholders, crowdsource design ideas and also preempt the problems of any complex urban planning project</p>

  <h2 class="abs label how-title">How it works!</h2>
  <p class="abs body how-intro">Plazamesh Kit brings together state-of-the-art geospatial technology and community workshops to enable collaborative urban planning. Here’s how:</p>

  <div class="step-icon" style="left:74px">
    <svg width="65" height="65" viewBox="0 0 65 65" aria-label="Chart icon" role="img">
      <rect x="17" y="17" width="30" height="28" fill="none" stroke="var(--icon-dark)" stroke-width="3"/>
      <polyline points="20,38 27,29 32,34 43,21" fill="none" stroke="var(--icon-dark)" stroke-width="2.5"/>
      <rect x="40" y="34" width="4" height="14" fill="var(--icon-dark)"/>
    </svg>
  </div>
  <div class="step-icon" style="left:234px" role="img" aria-label="Icon of people seated around a workshop table">
    <svg width="65" height="65" viewBox="0 0 65 65" aria-hidden="true">
      <ellipse cx="32.5" cy="40" rx="18" ry="5" fill="#fff" stroke="var(--icon-dark)" stroke-width="2.5"/>
    </svg>
  </div>
  <div class="step-icon" style="left:396px">
    <svg width="65" height="65" viewBox="0 0 65 65" aria-label="Integration icon" role="img">
      <rect x="16" y="16" width="33" height="33" rx="4" fill="none" stroke="var(--icon-dark)" stroke-width="3"/>
      <rect x="25" y="25" width="15" height="15" rx="2" fill="#fff" stroke="var(--icon-dark)" stroke-width="3"/>
      <circle cx="44" cy="44" r="6" fill="#fff" stroke="var(--icon-dark)" stroke-width="3"/>
    </svg>
  </div>

  <p class="step-caption body" style="left:51px"><span class="label">Set up</span> your project on plazameshkit.com, get your data in as well if you have it</p>
  <p class="step-caption body" style="left:210px">We <span class="label">conduct</span> community workshops &amp; crowdsource design ideas</p>
  <p class="step-caption body" style="left:370px">Designs are <span class="label">integrated</span> into your plazameshkit.com project</p>

  <p class="abs body lead">With the plazameshkit.com platform, you can!</p>

  <div class="feature body" style="left:34px;top:619px"><span class="label">Compare Designs and Impacts</span>The simple yet powerful interface enables advanced comparisons, synthesis of designs and their impacts</div>
  <div class="feature body" style="left:284px;top:619px"><span class="label">Collaborate on Urban Design</span>All designs churned out from the community are readily accessible for review and sharing</div>
  <div class="feature body" style="left:34px;top:684px"><span class="label">Get actionable data</span>Easily download, print or email single or multiple designs and integrate them into your project</div>
  <div class="feature body" style="left:284px;top:684px"><span class="label">Design for any scale</span>Address problems from a block level to a regional level</div>
</section>

<section class="page page--back">
  <header class="abs band">
    <h1 class="band__title">Hosted Community Workshops!</h1>
    <p class="band__text">We organize day-long planning workshops for experts and non-experts to come together and brainstorm on urban design plans.</p>
  </header>

  <div class="section body" style="left:30px;top:131px">
    <h3 class="section__head"><span class="num">1</span>THE FOUNDATION</h3>
    <div class="item"><span class="label">Groundwork</span>We work with you to investigate the project area &amp; identify all stakeholders</div>
    <div class="item"><span class="label">Creating interest</span>We excite participants to attend the planning workshop</div>
  </div>

  <div class="section body" style="left:30px;top:262px">
    <h3 class="section__head"><span class="num">2</span>THE WORKSHOP</h3>
    <div class="item"><span class="label">Organization</span>We get key stakeholders (no more than 15) to attend your workshop</div>
    <div class="item"><span class="label">Remote attendance</span>We also enable general public to participate over the internet</div>
    <div class="item"><span class="label">Tooling</span>We empower the participants with simple design tools &amp; implements</div>
    <div class="item"><span class="label">Goal setting</span>We establish goals and specific design requirements for participants</div>
  </div>

  <div class="section body" style="left:280px;top:131px">
    <h3 class="section__head"><span class="num">3</span>THE OUTCOME</h3>
    <div class="item"><span class="label">Designs</span>Participants can generate unique designs for each objective</div>
    <div class="item"><span class="label">Peer review</span>Designs are rated &amp; ranked by all participants independently</div>
    <div class="item"><span class="label">Discussion</span>The best designs are discussed and opinions are recorded</div>
  </div>

  <div class="section body" style="left:280px;top:309px">
    <h3 class="section__head"><span class="num">4</span>ACTIONABLES</h3>
    <div class="item"><span class="label">Report</span>We summarize key events &amp; opinions from the workshop into a report</div>
    <div class="item"><span class="label">Integration</span>Designs are integrated into your project on plazameshkit.com</div>
    <div class="item"><span class="label">Analysis</span>Urban planners can easily analyse the project and its outcomes</div>
  </div>

  <h2 class="abs when-title">When should you consider Plazamesh Kit?</h2>
  <p class="abs body when-text">Before you finalize a plan for your project. The goal is to get ideas &amp; opinions from all affected members and stakeholders before you expend time &amp; money in creating a formal proposal.</p>
  <h2 class="abs label accel-title">Accelerate your understanding</h2>
  <p class="abs body accel-text">The outcomes of a Plazamesh Kit project are designs and design ideas built collaboratively, taking into account diverse views and an advanced analysis of your planning problem.</p>

  <div class="abs callout">
    <h2 class="callout__title">Interested?</h2>
    <p class="callout__text">Plazamesh Kit is led by Tomas Verhoeven, PhD student at the Centre for Applied Spatial Study at Northmere University.</p>
    <p class="callout__email">Email: tomas@plazameshkit.com</p>
  </div>
  <div class="abs contact-ring"></div>
  <div class="abs contact-photo" role="img" aria-label="Portrait photo of the project lead"></div>
</section>

</body>
</html>
```